Design a Flyer for Comet Kid Day

Looking for a unique/cool flyer design for a kids super hero party.

I'll need an 8.5x11 flyer and a 4x6 matching in style image.

This should say: Fighting for Justice! Pursuing the Good! Striving for Awesome!

For any photos/images you need please use www.Pixelwharf.example I will purchase and attach any images for the winning designer. In the meantime, simply take a screen shot of the image you'd like to use, I understand the watermarks will be there, that's okay, we'll purchase the winning photos at the end.

Suggestions: Cool comic book style, maybe, mixed with a reality picture of a real kid?

I will need all photoshop work/source files in case there needs to be any edits, changes. There should be a space for a logo/day/date/time information. I appreciate if this can be incorporated INTO the design someway, and not just "added" if that makes sense.

Also, if you have questions post for clarification, I'll be quick to reply. Thank you :)

```html
<!DOCTYPE html>
<html lang="en">
<head>
<meta charset="UTF-8">
<title>Super Hero Party Flyer</title>
<link rel="stylesheet" href="https://fonts.googleapis.com/css2?family=Press+Start+2P&family=Audiowide&family=Arimo:wght@700&display=swap">
<style>
  :root {
    --night: #07040f;
    --magenta: #f01ab0;
    --hot-pink: #ff4fd2;
    --violet: #7a1fd0;
    --electric-blue: #1f6df2;
    --ice: #9fe4ff;
    --white: #ffffff;
    --steel: #b9b9b9;
    --sun-yellow: #fff200;
    --band: rgba(8, 6, 16, 0.8);
    --hair: #8a5530;
    --skin: #f2c6a6;
    --suit-red: #d8323a;
    --cape-orange: #f3a42c;
    --boot-blue: #3aa6e8;
  }
  * { margin: 0; padding: 0; box-sizing: border-box; }
  html, body {
    width: 835px;
    height: 1200px;
    overflow: hidden;
    background: var(--night);
  }
  .flyer {
    position: relative;
    width: 835px;
    height: 1200px;
    overflow: hidden;
    background: var(--night);
  }
  .backdrop-glow {
    position: absolute;
    inset: 0;
    background:
      radial-gradient(ellipse 340px 560px at 720px 480px, rgba(31,109,242,0.55), transparent 70%),
      radial-gradient(ellipse 320px 480px at 110px 640px, rgba(240,26,176,0.5), transparent 70%),
      radial-gradient(ellipse 280px 260px at 430px 420px, rgba(122,31,208,0.45), transparent 70%),
      linear-gradient(180deg, #04020a 0%, #110722 55%, #0a0514 100%);
  }
  .light-streaks {
    position: absolute;
    inset: 0;
    width: 835px;
    height: 1200px;
  }
  .slogans {
    position: absolute;
    top: 34px;
    left: 0;
    width: 100%;
    text-align: center;
    font-family: "Press Start 2P", monospace;
    font-weight: 400;
    font-size: 33px;
    line-height: 62px;
    color: var(--white);
    letter-spacing: 1px;
    text-shadow: 0 0 3px var(--electric-blue), 0 0 8px var(--electric-blue), 2px 2px 0 #0d2a8a;
  }
  .hero-shadow {
    position: absolute;
    left: 330px;
    top: 700px;
    width: 300px;
    height: 110px;
    border-radius: 50%;
    background: rgba(0, 0, 0, 0.75);
  }
  .hero-art {
    position: absolute;
    left: 228px;
    top: 225px;
    width: 365px;
    height: 645px;
    border-radius: 150px 150px 60px 60px;
    background:
      linear-gradient(90deg, rgba(243,164,44,0) 0%, rgba(243,164,44,0.55) 100%),
      linear-gradient(180deg,
        var(--hair) 0%,
        var(--hair) 14%,
        var(--skin) 20%,
        var(--skin) 27%,
        var(--suit-red) 34%,
        var(--boot-blue) 52%,
        var(--suit-red) 60%,
        var(--suit-red) 78%,
        var(--boot-blue) 86%,
        var(--boot-blue) 100%);
    box-shadow: 0 0 30px rgba(255, 255, 255, 0.12);
  }
  .title {
    position: absolute;
    top: 896px;
    left: 0;
    width: 100%;
    text-align: center;
    font-family: "Audiowide", sans-serif;
    font-weight: 400;
    font-size: 104px;
    line-height: 96px;
    letter-spacing: 1px;
  }
  .title-line {
    display: block;
    background: linear-gradient(180deg, #ffffff 0%, #e2e2e2 45%, #a5a5a5 58%, #efefef 100%);
    -webkit-background-clip: text;
    background-clip: text;
    -webkit-text-fill-color: transparent;
    filter: drop-shadow(3px 4px 2px rgba(0,0,0,0.85));
  }
  .event-details {
    position: absolute;
    left: 0;
    bottom: 0;
    width: 100%;
    height: 86px;
    background: var(--band);
    display: flex;
    align-items: center;
    justify-content: center;
    font-family: "Arimo", sans-serif;
    font-weight: 700;
    font-size: 50px;
    color: var(--sun-yellow);
  }
</style>
</head>
<body>
  <main class="flyer">
    <div class="backdrop-glow"></div>
    <svg class="light-streaks" viewBox="0 0 835 1200" aria-hidden="true">
      <defs>
        <filter id="glow" x="-20%" y="-20%" width="140%" height="140%">
          <feGaussianBlur stdDeviation="6"/>
        </filter>
        <filter id="soft-glow" x="-20%" y="-20%" width="140%" height="140%">
          <feGaussianBlur stdDeviation="18"/>
        </filter>
      </defs>
      <g fill="none" stroke-linecap="round">
        <g filter="url(#soft-glow)" opacity="0.8">
          <path d="M0 380 C240 460 300 720 835 900" stroke="#f01ab0" stroke-width="70"/>
          <path d="M420 260 C640 300 600 640 835 820" stroke="#1f6df2" stroke-width="80"/>
          <path d="M260 300 C420 240 520 420 620 700" stroke="#7a1fd0" stroke-width="50"/>
        </g>
        <g filter="url(#glow)">
          <path d="M0 330 C250 420 300 700 835 880" stroke="#ff4fd2" stroke-width="10" opacity="0.9"/>
          <path d="M0 430 C200 530 270 770 835 960" stroke="#f01ab0" stroke-width="16" opacity="0.85"/>
          <path d="M0 560 C180 660 350 830 835 1010" stroke="#ff4fd2" stroke-width="8" opacity="0.8"/>
          <path d="M0 680 C160 760 340 900 760 1100" stroke="#c0149a" stroke-width="12" opacity="0.7"/>
          <path d="M380 260 C600 300 560 650 835 820" stroke="#1f6df2" stroke-width="14" opacity="0.9"/>
          <path d="M470 230 C700 260 650 600 835 700" stroke="#9fe4ff" stroke-width="6" opacity="0.85"/>
          <path d="M420 300 C560 420 700 800 835 920" stroke="#5fb8ff" stroke-width="10" opacity="0.8"/>
          <path d="M540 200 C760 230 720 480 835 560" stroke="#1f6df2" stroke-width="8" opacity="0.7"/>
          <path d="M330 1200 C380 1060 440 960 500 880" stroke="#ffffff" stroke-width="6" opacity="0.45"/>
          <path d="M420 1200 C450 1080 490 990 540 900" stroke="#9fe4ff" stroke-width="5" opacity="0.45"/>
          <path d="M230 1200 C300 1080 380 980 460 900" stroke="#ff4fd2" stroke-width="6" opacity="0.5"/>
        </g>
      </g>
    </svg>
    <h2 class="slogans">FIGHTING FOR JUSTICE!<br>PURSUING THE GOOD!<br>STRIVING FOR AWESOME!</h2>
    <div class="hero-shadow"></div>
    <div class="hero-art" role="img" aria-label="Cartoon girl superhero with brown hair, red and blue suit, orange cape and blue boots, hands on hips"></div>
    <h1 class="title"><span class="title-line">SUPER HERO</span><span class="title-line">PARTY</span></h1>
    <p class="event-details">August 21, 2014 @ Some Place</p>
  </main>
</body>
</html>
```